■素材
・ディレクトリマップ
・ロゴ
・コーポレート掲載情報概要

上記のデータはこちらからダウンロードをお願いします。
https://23.dorevault.example/0805-f41a9e27d05b8c3e6a71d2b94c0e58af2

※レスポンシブを想定したデザインでお願いします。
※スマホがメインデバイスです

少ないですが、現サイトの素材はどれも使って頂いて構いません。
その他、採用された場合はソルベンなどの素材サイトでも購入できますので、
カンプデータで制作いただけるとイメージがしやすいので助かります。

■参考サイト
ポイント:シンプルデザインと、シンプルUI、コンテンツ量の参考
https://fernquil.co.jp/
https://about.marobe.jp/company/

■依頼背景
webメディア「Vexora」を運営する会社です。「卓球は人をつなぐ。」をテーマに、選手との取組みをはじめ、卓球場やイベントのマネジメント、プロモーション、物販など幅広いサービスを展開しております。今年はさらに新規サービスをいくつか立ち上げる予定です。
また、これら事業を進める中で私達が大切にしていることは、「卓球」のリブランディングです。
ダサく、狭いコミュニティであるというイメージを払拭し、卓球本来の特徴でもある、3歳〜90歳までが楽しめるカジュアルなスポーツとして、卓球に触れるハードルを下げたいと思っています。
そのためには、かっこ良く、多少ファッショナブルな、エンタメ要素やスタイリッシュさも必要だと思っています。
コーポレートサイトでは、上記のような事を私達が率先して実践していく、というような、所謂”今っぽい”見せ方ができるサイトにしたいと思っています。

その他ご不明な点があれば、お気軽にご質問ください。

以上となります。
何卒よろしくお願い致します。
https://lumitora.jp/
2ページ
グレー系、スタイリッシュにカッコよく見せたいです
• 高解像度JPG (.jpg)
• イラストレーター形式 (.ai)
• フォトショップ形式 (.psd)
フォトショ、イラレどちらか一方で構いません。
新規事業立上げにつき、宜しければ継続的にお仕事ができるパートナーになれると嬉しいです
※スマホでのデザイン提案をお願い致します。

前に出過ぎない「卓球」の存在感と、カジュアルなイメージが決定打でした。
そのため、ガチでも素人でもどんな相手でも受け入れられる許容の幅が広く、かつセンスが感じられました。
このTOPページデザインのように、誰でも楽しく気軽にピンポンする。という場面が多く見れるように、事業を育てたいと思います。

この度は、弊社のための貴重なお時間を使ってくださり、ありがとうございました。卓球を全然知らない方にとっては、新鮮な案件だったのでは無いでしょうか。案件の依頼概要にも書きましたが、卓球をかっこよくおしゃれにリブランディングしていく予定です。そのため、また依頼をさせて頂くこともあるかと思いますので、今回ご応募頂いた方で、残念ながらご縁が無かった方も、引き続き宜しくお願い致します。まずは弊社にお時間を使ってくださったことに感謝申し上げます。ありがとうございました。森野

```html
<!DOCTYPE html>
<html lang="ja">
<head>
<meta charset="utf-8">
<title>LUMITORA</title>
<link href="https://fonts.googleapis.com/css2?family=Montserrat:wght@600;800&family=Noto+Sans+JP:wght@300&display=swap" rel="stylesheet">
<style>
  :root {
    --bg: #000000;
    --ink: #ffffff;
    --photo-dark: #0b0b0b;
    --photo-mid: #3a3a3a;
    --photo-light: #8a8a8a;
  }
  html, body {
    margin: 0;
    padding: 0;
    width: 675px;
    height: 1200px;
    overflow: hidden;
    background: var(--bg);
  }
  .page {
    position: relative;
    width: 675px;
    height: 1200px;
    background: var(--bg);
    color: var(--ink);
    font-family: "Montserrat", sans-serif;
  }
  .site-title {
    position: absolute;
    top: 78px;
    left: 0;
    width: 100%;
    margin: 0;
    text-align: center;
    font-weight: 600;
    font-size: 48px;
    letter-spacing: 8px;
  }
  .hero-photo {
    position: absolute;
    top: 380px;
    left: 0;
    width: 675px;
    height: 380px;
    background:
      radial-gradient(circle at 189px 423px, #f08a1c 0, #d8560a 38px, transparent 41px) no-repeat,
      radial-gradient(ellipse 300px 70px at 360px 270px, var(--photo-mid), transparent 100%),
      radial-gradient(ellipse 160px 90px at 600px 280px, var(--photo-light), transparent 100%),
      var(--photo-dark);
    background-position: 0 -380px, 0 0, 0 0, 0 0;
  }
  .tagline {
    position: absolute;
    top: 210px;
    left: 316px;
    margin: 0;
    writing-mode: vertical-rl;
    font-family: "Noto Sans JP", sans-serif;
    font-weight: 300;
    font-size: 40px;
    letter-spacing: 6px;
    color: var(--ink);
  }
  .main-nav {
    position: absolute;
    top: 806px;
    left: 0;
    width: 100%;
  }
  .main-nav ul {
    list-style: none;
    margin: 0;
    padding: 0;
    text-align: center;
  }
  .main-nav li {
    font-weight: 800;
    font-size: 44px;
    line-height: 77px;
    letter-spacing: 1px;
  }
  .social {
    position: absolute;
    top: 1064px;
    left: 0;
    width: 100%;
    display: flex;
    justify-content: center;
    align-items: center;
    gap: 34px;
    font-weight: 800;
    font-size: 22px;
  }
  .social svg { display: block; }
</style>
</head>
<body>
  <div class="page">
    <h1 class="site-title">LUMITORA</h1>

    <div class="hero-photo" role="img" aria-label="Black and white photo of a hand holding a table tennis paddle with an orange ball in the air"></div>

    <p class="tagline">卓球は人をつなぐ。</p>

    <nav class="main-nav">
      <ul>
        <li>ABOUTO</li>
        <li>SERVICE</li>
        <li>NEWS</li>
      </ul>
    </nav>

    <div class="social">
      <span class="social-link">Chirply</span>
      <span class="social-link">Folio</span>
      <svg class="feed-icon" width="44" height="44" viewBox="0 0 44 44" aria-label="Feed">
        <rect x="0" y="0" width="44" height="44" rx="8" fill="var(--ink)"/>
        <circle cx="13" cy="31" r="4" fill="var(--bg)"/>
        <path d="M9 19 A16 16 0 0 1 25 35" stroke="var(--bg)" stroke-width="4.5" fill="none"/>
        <path d="M9 9 A26 26 0 0 1 35 35" stroke="var(--bg)" stroke-width="4.5" fill="none"/>
      </svg>
    </div>
  </div>
</body>
</html>
```